brovalux business card

We are a commercial cleaning/janitorial service company our main target is building owners and managers.
Would like to see the icon as a background shadow in the front and the full logo in white on the back with a blue background.  On the card:
Dorn Pevsky, Operations Manager, dorn@brovalux-example.com
47215-K Harlow Ave. 9 #382
Pinecrest, IN 47912
555.604.2817, 888.555.4163

Updates
please include cell 555.318.6247
                                   
Thank you
If possible the fading logo on the front should be very subtle and light and lets look at centering that as well
thanks

```html
<!DOCTYPE html>
<html lang="en">
<head>
<meta charset="utf-8">
<title>brovalux business card</title>
<link rel="stylesheet" href="https://fonts.googleapis.com/css2?family=Lato:wght@400;700&display=swap">
<style>
  :root {
    --stage: #e9ecef;
    --card-white: #ffffff;
    --brand-blue: #2272bd;
    --ink: #3a3a3a;
    --ink-soft: #555555;
    --accent-bar: #4a4646;
    --ghost-mark: #f1f3f6;
    --white: #ffffff;
  }
  * { box-sizing: border-box; margin: 0; padding: 0; }
  html, body {
    width: 1200px; height: 960px; overflow: hidden;
    background: var(--stage);
    font-family: "Lato", sans-serif;
  }
  .stage {
    width: 1200px; height: 960px;
    display: flex; flex-direction: column;
    align-items: center; justify-content: center; gap: 56px;
  }
  .card {
    position: relative;
    width: 700px; height: 400px;
    overflow: hidden;
    box-shadow: 0 6px 18px rgba(0,0,0,0.12);
  }

  /* Front */
  .card-front { background: var(--card-white); color: var(--ink); }
  .ghost-mark {
    position: absolute; left: 50%; top: 50%;
    width: 300px; height: 300px; margin: -150px 0 0 -150px;
    border-radius: 50%; background: var(--ghost-mark);
  }
  .name-bar {
    position: absolute; left: 0; top: 88px;
    width: 14px; height: 78px; background: var(--accent-bar);
  }
  .identity { position: absolute; left: 40px; top: 86px; }
  .person-name {
    font-size: 38px; font-weight: 400; letter-spacing: 0.5px;
    text-transform: uppercase; line-height: 1.1;
  }
  .person-title { font-size: 22px; color: var(--ink-soft); margin-top: 6px; }
  .contact-list {
    position: absolute; left: 40px; bottom: 34px;
    list-style: none; font-size: 21px; line-height: 30px; color: var(--ink);
  }
  .contact-list li { display: flex; align-items: center; gap: 14px; }
  .contact-icon { width: 18px; height: 18px; flex: none; }
  .address {
    position: absolute; right: 44px; top: 232px;
    font-size: 18px; line-height: 26px; color: var(--ink-soft);
  }

  /* Back */
  .card-back {
    background: var(--brand-blue); color: var(--white);
    display: flex; align-items: center; justify-content: center;
  }
  .brand-lockup { display: flex; align-items: center; gap: 22px; }
  .brand-dot { width: 84px; height: 84px; border-radius: 50%; background: var(--white); }
  .brand-name { font-size: 76px; font-weight: 700; line-height: 0.9; letter-spacing: 1px; }
  .brand-tagline { font-size: 20px; font-weight: 700; letter-spacing: 3px; margin-top: 4px; }
  .edge-tab {
    position: absolute; right: 0; top: 150px;
    width: 12px; height: 58px; background: var(--accent-bar);
  }
</style>
</head>
<body>
<main class="stage">
  <section class="card card-front" aria-label="Business card front">
    <div class="ghost-mark" aria-hidden="true"></div>
    <div class="name-bar"></div>
    <div class="identity">
      <h1 class="person-name">Dorn Pevsky</h1>
      <p class="person-title">Operations Manager</p>
    </div>
    <p class="address">47215-K Harlow Ave. 9 #382<br>Pinecrest, IN 47912</p>
    <ul class="contact-list">
      <li>
        <svg class="contact-icon" viewBox="0 0 18 18" aria-hidden="true"><rect x="4" y="1" width="10" height="16" rx="1.5" fill="none" stroke="#444" stroke-width="1.6"/><rect x="6" y="3.5" width="6" height="5" fill="#444"/><circle cx="9" cy="13" r="1.2" fill="#444"/></svg>
        <span>555.604.2817</span>
      </li>
      <li>
        <svg class="contact-icon" viewBox="0 0 18 18" aria-hidden="true"><rect x="4" y="1" width="10" height="16" rx="1.5" fill="none" stroke="#444" stroke-width="1.6"/><rect x="6" y="3.5" width="6" height="5" fill="#444"/><circle cx="9" cy="13" r="1.2" fill="#444"/></svg>
        <span>888.555.4163</span>
      </li>
      <li>
        <svg class="contact-icon" viewBox="0 0 18 18" aria-hidden="true"><rect x="4" y="1" width="10" height="16" rx="1.5" fill="none" stroke="#444" stroke-width="1.6"/><rect x="6" y="3.5" width="6" height="5" fill="#444"/><circle cx="9" cy="13" r="1.2" fill="#444"/></svg>
        <span>555.318.6247</span>
      </li>
      <li>
        <svg class="contact-icon" viewBox="0 0 18 18" aria-hidden="true"><rect x="1" y="3.5" width="16" height="11" fill="none" stroke="#444" stroke-width="1.6"/><path d="M1 3.5 9 10 17 3.5M1 14.5 7 8.5M17 14.5 11 8.5" fill="none" stroke="#444" stroke-width="1.4"/></svg>
        <span>dorn@brovalux-example.com</span>
      </li>
    </ul>
  </section>

  <section class="card card-back" aria-label="Business card back">
    <div class="brand-lockup">
      <div class="brand-dot" aria-hidden="true"></div>
      <div>
        <p class="brand-name">brovalux</p>
        <p class="brand-tagline">Building Services</p>
      </div>
    </div>
    <div class="edge-tab"></div>
  </section>
</main>
</body>
</html>
```